Menu Board 1000mmx500mm re-design

I would like to re-design exiting menu board 1000mmx500mm. Current board letters are bit to small to read. I would like to have pictures (attached) of the food offered on it and at the same time to create balance between pictures and size of the text to be easily readable. Fonts and colours are up to designer choice but prefer warm and bright colours rather anything dark.

Target Market(s)

Food industry

Industry/Entity Type

Food

Font styles to use
Other font styles liked:
• I leave font choice to designer

Colors
FFC000
F8CF3A
FAE287
FDF2CF
FEFAEE
F0912C
F2A743
F7CA91
FBE8D2
FDF5EE
EE7325
F08F49
F5BC92
FAE3D3
FDF4ED

Requirements
Must have
• Pictures + Text
Nice to have
• Balance between images and text.
Should not have
• Can't think of any

```html
<!DOCTYPE html>
<html lang="en">
<head>
<meta charset="utf-8">
<title>Menu Board</title>
<link href="https://fonts.googleapis.com/css2?family=Permanent+Marker&family=Montserrat:wght@700;800&family=Lato:wght@400&family=Anton&display=swap" rel="stylesheet">
<style>
:root{
  --orange:#E2540F;
  --orange-deep:#C9460A;
  --white:#FFFFFF;
  --ink:#111111;
  --wrap-tone:#D9B27A;
  --wrap-tone-2:#8E6A3C;
  --beet-tone:#8C2F45;
  --beet-tone-2:#D9C7B0;
  --plate-tone:#8A4A1E;
  --chicken-tone:#D8963F;
  --potato-tone:#E7B14E;
  --potato-tone-2:#9C6A22;
}
*{margin:0;padding:0;box-sizing:border-box}
html,body{width:1200px;height:2400px;overflow:hidden;background:var(--white)}
.board{position:relative;width:1200px;height:2400px;background:var(--white);overflow:hidden;font-family:'Lato',sans-serif;color:var(--white)}
.hero{position:absolute;left:0;top:0;width:1200px;height:800px}
.menu-title{position:absolute;left:0;top:790px;width:1200px;text-align:center;font-family:'Permanent Marker',cursive;font-size:250px;line-height:1;color:var(--orange);letter-spacing:4px}
.band{position:absolute;background:var(--orange);clip-path:polygon(1% 3%,40% 0,99% 2%,100% 50%,99.5% 97%,60% 100%,0 98%,0.5% 50%)}
.item-name{font-family:'Montserrat',sans-serif;font-weight:800;letter-spacing:1px;line-height:1}
.item-price{position:absolute;font-family:'Montserrat',sans-serif;font-weight:800;line-height:1}
.item-desc{font-size:25px;line-height:1.2;margin-top:6px}
.photo{position:absolute}
.band-ciabatta{left:576px;top:1078px;width:552px;height:146px;padding:26px 0 0 26px}
.band-wrap{left:576px;top:1230px;width:552px;height:124px;padding:14px 0 0 26px}
.band-ciabatta .item-name,.band-wrap .item-name{font-size:37px}
.band-ciabatta .item-price,.band-wrap .item-price{font-size:40px;right:36px}
.band-ciabatta .item-price{top:24px}
.band-wrap .item-price{top:12px}
.band-beet{left:150px;top:1392px;width:714px;height:204px;padding:56px 0 0 138px;clip-path:polygon(4% 8%,50% 0,100% 4%,100% 96%,50% 100%,2% 94%,0 50%)}
.band-beet .item-name{font-size:40px;display:inline-block}
.band-beet .item-price{position:static;display:inline-block;font-size:42px;margin-left:34px}
.band-beet .item-desc{font-size:27px;margin-top:14px}
.band-quarter{left:276px;top:1632px;width:768px;height:132px;padding:42px 0 0 158px}
.band-half{left:240px;top:1776px;width:834px;height:138px;padding:36px 0 0 194px}
.band-quarter .item-name,.band-half .item-name{font-size:40px}
.band-quarter .item-price{left:626px;top:40px;font-size:44px}
.band-half .item-price{left:648px;top:34px;font-size:44px}
.band-half .item-desc{font-size:27px;margin-top:12px}
.band-sides{left:144px;top:1962px;width:768px;height:228px;padding:34px 0 0 90px}
.side-row{position:relative;font-family:'Montserrat',sans-serif;font-weight:800;font-size:32px;line-height:1}
.side-row .item-price{font-size:34px}
.side-note{font-size:22px;margin-top:6px}
.footer{position:absolute;left:0;top:2250px;width:1200px;height:150px;background:var(--orange);color:var(--ink)}
.footer-title{position:absolute;left:64px;top:10px;font-family:'Anton',sans-serif;font-size:128px;line-height:1;letter-spacing:2px}
.sauce{position:absolute;font-family:'Montserrat',sans-serif;font-weight:800;font-size:33px;line-height:1}
</style>
</head>
<body>
<main class="board">
  <svg class="hero" viewBox="0 0 1200 800" xmlns="http://www.w3.org/2000/svg">
    <path d="M0 0 H150 C250 120 120 250 110 420 C100 600 260 700 420 690 C620 680 760 650 900 680 C1020 700 1120 640 1160 560 C1180 500 1200 450 1200 440 V720 C1140 770 1040 790 900 770 C760 750 600 790 420 788 C240 786 40 700 18 500 C0 320 110 200 40 80 C30 60 10 30 0 20 Z" fill="var(--orange)"/>
    <defs>
      <linearGradient id="wrapGrad" x1="0" y1="0" x2="1" y2="1">
        <stop offset="0" stop-color="var(--wrap-tone)"/>
        <stop offset="1" stop-color="var(--wrap-tone-2)"/>
      </linearGradient>
    </defs>
    <path role="img" aria-label="Photo of a grilled vegetable wrap cut in half and stacked" d="M160 0 H1200 V440 C1150 520 1100 600 1000 640 C860 690 720 650 560 680 C420 705 260 690 180 600 C110 520 120 420 130 320 C140 200 220 110 160 0 Z" fill="url(#wrapGrad)"/>
  </svg>

  <h1 class="menu-title">MENU</h1>

  <svg class="photo" style="left:18px;top:1080px" width="552" height="264" viewBox="0 0 552 264">
    <ellipse role="img" aria-label="Photo of a grilled chicken slaw wrap on a wooden board" cx="276" cy="150" rx="272" ry="108" fill="var(--wrap-tone)"/>
  </svg>
  <div class="band band-ciabatta">
    <div class="item-name">CIABATTA</div><div class="item-price">£6</div>
    <p class="item-desc">Roti Chicken, Rucola, Caramelized Onions.<br>Tomato, Fresh Onion</p>
  </div>
  <div class="band band-wrap">
    <div class="item-name">WRAP</div><div class="item-price">£7</div>
    <p class="item-desc">Roti Chicken, Crunchy Slaw, Tomato,<br>Fresh Onion &amp; Sauce of your choice</p>
  </div>

  <div class="band band-beet">
    <div class="item-name">BEETROOT WRAP</div><div class="item-price">£8</div>
    <p class="item-desc">Roti Chicken, Crunchy Slaw, Tomato,<br>Fresh Onion &amp; Sauce of your choice</p>
  </div>
  <svg class="photo" style="left:828px;top:1368px" width="342" height="252" viewBox="0 0 342 252">
    <defs><linearGradient id="beetGrad" x1="0" y1="0" x2="1" y2="1"><stop offset="0" stop-color="var(--beet-tone-2)"/><stop offset="1" stop-color="var(--beet-tone)"/></linearGradient></defs>
    <ellipse role="img" aria-label="Photo of a beetroot wrap cut in half" cx="171" cy="126" rx="168" ry="122" fill="url(#beetGrad)"/>
  </svg>

  <div class="band band-quarter">
    <div class="item-name">1/4 CHICKEN BOX</div><div class="item-price">£9</div>
  </div>
  <div class="band band-half">
    <div class="item-name">1/2 CHICKEN BOX</div><div class="item-price">£14</div>
    <p class="item-desc">Roti Chicken, Veggie Rice &amp; Salad</p>
  </div>
  <svg class="photo" style="left:48px;top:1620px" width="348" height="288" viewBox="0 0 348 288">
    <defs><radialGradient id="plateGrad"><stop offset="0.45" stop-color="var(--chicken-tone)"/><stop offset="1" stop-color="var(--plate-tone)"/></radialGradient></defs>
    <ellipse role="img" aria-label="Photo of roast chicken leg with veggie rice on a wooden plate" cx="174" cy="144" rx="172" ry="140" fill="url(#plateGrad)"/>
  </svg>

  <div class="band band-sides">
    <div class="side-row">ROASTED POTATOES <span class="item-price" style="left:388px;top:-2px">£2.5</span></div>
    <p class="side-note">Thyme &amp; Garlic</p>
    <div class="side-row" style="margin-top:42px">WATER <span class="item-price" style="left:400px;top:-30px">£1</span></div>
    <div class="side-row" style="margin-top:6px">CAN &amp; JUICES <span class="item-price" style="left:372px;top:0">£1.8</span></div>
  </div>
  <svg class="photo" style="left:850px;top:1932px" width="288" height="288" viewBox="0 0 288 288">
    <defs><radialGradient id="potatoGrad"><stop offset="0.3" stop-color="var(--potato-tone)"/><stop offset="1" stop-color="var(--potato-tone-2)"/></radialGradient></defs>
    <circle role="img" aria-label="Photo of roasted potatoes with thyme" cx="144" cy="144" r="142" fill="url(#potatoGrad)"/>
  </svg>

  <footer class="footer">
    <div class="footer-title">SAUCES</div>
    <span class="sauce" style="left:548px;top:44px">SIGNATURE</span>
    <span class="sauce" style="left:548px;top:80px">SWEET CHILLI</span>
    <span class="sauce" style="left:840px;top:44px">BBQ</span>
    <span class="sauce" style="left:840px;top:80px">GARLIC</span>
    <span class="sauce" style="left:1002px;top:44px">PIRI PIRI</span>
    <span class="sauce" style="left:1002px;top:80px">MAYO</span>
  </footer>
</main>
</body>
</html>
```